Business Card Design Project Massage Shop

Business card for Foot, Hot Stone and Full body Massage. I am thinking photo for the front. Back should say "$20 off 1hr basic service" "Offer not valid with any other coupons or offers"

Target Market(s)

Women wanting good quality massage

Industry/Entity Type

Business

Contact Information for Business Card

816.472.3908
27815 W 12 Hwy
Harlow Mo 64118

www.lanternmassage.co

Other font styles liked:
• http://www.typequarry.net/fonts/brelwick/no.-seven/

Colors
0455a3

Requirements
Must have
• The business name "Lantern Massage" must be in this font and a royal blue color http://www.typequarry.net/fonts/brelwick/no.-seven/
• The remaining information must be more readable.
Should not have
• the web site is .co
• Not a .com
• should not look like it was done on a prindle or someothere website.

```html
<!DOCTYPE html>
<html lang="en">
<head>
<meta charset="utf-8">
<title>Lantern Massage – Business Card</title>
<link href="https://fonts.googleapis.com/css2?family=Source+Sans+3:wght@400;600;700&display=swap" rel="stylesheet">
<style>
  :root {
    --backdrop: #ecebe8;
    --royal-card: #0202a0;
    --royal-ink: #1b1b9e;
    --paper: #ffffff;
    --rule: #e8d9cb;
    --badge-grey: #8d8d8f;
    --badge-ring: #6b4a9a;
    --shadow: rgba(0, 0, 0, 0.18);
  }
  * { margin: 0; padding: 0; box-sizing: border-box; }
  html, body {
    width: 1200px; height: 900px; overflow: hidden;
    background: var(--backdrop);
    font-family: "Source Sans 3", "Myriad Pro", sans-serif;
  }
  .canvas { position: relative; width: 1200px; height: 900px; }

  .card {
    position: absolute;
    box-shadow: 0 6px 18px var(--shadow);
  }
  .card-front {
    left: 238px; top: 62px; width: 555px; height: 342px;
    background: var(--royal-card);
    color: var(--paper);
  }
  .card-back {
    left: 457px; top: 518px; width: 560px; height: 343px;
    background: var(--paper);
    color: var(--royal-ink);
  }

  .brand {
    position: absolute;
    display: flex; align-items: center; gap: 14px;
    white-space: nowrap;
  }
  .brand-name {
    font-weight: 600;
    font-size: 40px;
    line-height: 1;
  }
  .brand-dot {
    width: 46px; height: 46px; border-radius: 50%;
    flex: none;
  }
  .card-front .brand { left: 50%; top: 124px; transform: translateX(-50%); }
  .card-front .brand-name { color: var(--paper); }
  .card-front .brand-dot { background: var(--paper); }
  .card-back .brand { left: 50%; top: 114px; transform: translateX(-50%); }
  .card-back .brand-name { color: var(--royal-ink); }
  .card-back .brand-dot { background: var(--badge-grey); border: 3px solid var(--badge-ring); }

  .address {
    position: absolute; right: 293px; top: 213px;
    text-align: right; font-style: normal; font-size: 16px; line-height: 23px;
  }
  .contact {
    position: absolute; left: 290px; top: 211px;
    list-style: none; font-size: 16px; line-height: 23px;
  }
  .contact li { display: flex; align-items: center; gap: 9px; }
  .contact svg { width: 12px; height: 12px; flex: none; }

  .offer-line {
    position: absolute; left: 0; right: 0; top: 199px;
    display: flex; align-items: center; gap: 14px;
  }
  .offer-line::before, .offer-line::after {
    content: ""; flex: 1; height: 1px; background: var(--rule);
  }
  .offer-line p { font-size: 20px; font-weight: 600; white-space: nowrap; }
  .offer-line .amount { font-size: 24px; font-weight: 700; }
  .terms {
    position: absolute; left: 0; right: 0; top: 240px;
    text-align: center; font-size: 20px; font-weight: 600; line-height: 23px;
  }
</style>
</head>
<body>
<main class="canvas">
  <section class="card card-front" aria-label="Card front">
    <div class="brand">
      <span class="brand-name">Lantern Massage</span>
      <span class="brand-dot"></span>
    </div>
    <address class="address">27815 W 12 Hwy<br>Harlow Mo 64118</address>
    <ul class="contact">
      <li>
        <svg viewBox="0 0 24 24" aria-hidden="true"><path fill="#fff" d="M6.6 10.8a15 15 0 0 0 6.6 6.6l2.2-2.2a1 1 0 0 1 1-.25 11.4 11.4 0 0 0 3.6.6 1 1 0 0 1 1 1V20a1 1 0 0 1-1 1A17 17 0 0 1 3 4a1 1 0 0 1 1-1h3.5a1 1 0 0 1 1 1 11.4 11.4 0 0 0 .6 3.6 1 1 0 0 1-.25 1z"/></svg>
        <span>816.472.3908</span>
      </li>
      <li>
        <svg viewBox="0 0 24 24" aria-hidden="true"><g fill="none" stroke="#fff" stroke-width="2.6" stroke-linecap="round"><path d="M10 14a4.5 4.5 0 0 0 6.4 0l3.2-3.2a4.5 4.5 0 0 0-6.4-6.4l-1.4 1.4"/><path d="M14 10a4.5 4.5 0 0 0-6.4 0l-3.2 3.2a4.5 4.5 0 0 0 6.4 6.4l1.4-1.4"/></g></svg>
        <span>www.lanternmassage.co</span>
      </li>
    </ul>
  </section>

  <section class="card card-back" aria-label="Card back">
    <div class="brand">
      <span class="brand-name">Lantern Massage</span>
      <span class="brand-dot"></span>
    </div>
    <div class="offer-line">
      <p><span class="amount">$20</span> off Next 1hr + Basic Service</p>
    </div>
    <p class="terms">Offer not valid with any other<br>coupons or offers</p>
  </section>
</main>
</body>
</html>
```